Tamborine Ridge Country Club Business Sponsorship Package

Need a flyer to promote new business sponsorship packageCost 4500 + GST12 months sponsorship and promotion via TRCC Corporate Partners listing $1000 Food & Beverage House AccountMembers Welcome PackChristmas Party Invite7 Day with Cart Golf Membership10% discount on events and showsPayable over 4 installments

Target Market(s)

Business Owners who play Golf

Industry/Entity Type

Golf Course

```html
<!DOCTYPE html>
<html lang="en">
<head>
<meta charset="utf-8">
<title>Tamborine Ridge Country Club – Business Sponsorship Package</title>
<link rel="stylesheet" href="https://fonts.googleapis.com/css2?family=Roboto:wght@400;500;700&family=Roboto+Condensed:wght@400;500;700&display=swap">
<style>
  :root {
    --stage: #e6e7e8;
    --ink: #153a4a;
    --ink-dark: #0f2a36;
    --teal: #3e8a7c;
    --teal-soft: rgba(62, 138, 124, 0.92);
    --white: #ffffff;
    --sky-top: #f4f6f9;
    --sky-mid: #8fb3d6;
    --sky-low: #4f86bd;
    --tree: #3c5a36;
    --grass: #4f8a2e;
    --grass-deep: #2f5e1c;
  }
  * { box-sizing: border-box; margin: 0; padding: 0; }
  html, body { width: 1200px; height: 1200px; overflow: hidden; }
  body { background: var(--stage); position: relative; font-family: "Roboto Condensed", sans-serif; }

  .flyer {
    position: absolute; left: 150px; top: 17px;
    width: 900px; height: 1165px; overflow: hidden;
  }
  .flyer__scene {
    position: absolute; inset: 0;
    background: linear-gradient(180deg,
      var(--sky-top) 0%, #dce6f0 10%, var(--sky-mid) 24%, var(--sky-low) 40%,
      #9fbfd9 62%, var(--tree) 70%, var(--grass) 76%, var(--grass-deep) 100%);
  }

  .brand {
    position: absolute; top: 128px; left: 0; width: 100%;
    text-align: center;
    font-family: "Roboto", sans-serif; font-weight: 500;
    font-size: 34px; letter-spacing: 1px; color: var(--ink-dark);
  }
  .title {
    position: absolute; top: 250px; left: 0; width: 100%; text-align: center;
    font-family: "Roboto", sans-serif; font-weight: 700; font-size: 47px;
    color: var(--ink); letter-spacing: 0.5px;
  }
  .subtitle {
    position: absolute; top: 314px; left: 0; width: 100%; text-align: center;
    font-family: "Roboto", sans-serif; font-weight: 400; font-size: 28px;
    color: var(--ink-dark); letter-spacing: 25px; padding-left: 25px;
  }

  .offer {
    position: absolute; left: 262px; top: 371px; width: 396px; height: 490px;
    background: linear-gradient(180deg, var(--teal-soft) 0%, rgba(62,138,124,0.75) 35%, rgba(255,255,255,0.55) 75%, rgba(255,255,255,0) 100%);
  }
  .offer__frame {
    position: absolute; left: 20px; top: 19px; width: 354px; height: 460px;
    border: 3px solid var(--white); border-bottom: none;
  }
  .offer__rule { position: absolute; left: 46px; width: 309px; height: 2px; background: var(--ink-dark); opacity: 0.7; }

  .cost__label {
    position: absolute; left: 32px; top: 48px; transform: rotate(-90deg);
    font-size: 15px; color: var(--white); letter-spacing: 1px;
  }
  .cost__amount { position: absolute; left: 72px; top: 30px; font-weight: 700; font-size: 56px; color: var(--white); }
  .cost__term { position: absolute; left: 190px; top: 61px; font-size: 20px; color: var(--white); }

  .promo__line { position: absolute; left: 0; width: 100%; text-align: center; color: var(--ink-dark); }
  .promo__lead { top: 113px; font-size: 22px; }
  .promo__via { top: 126px; font-size: 26px; }
  .promo__via strong { font-family: "Roboto", sans-serif; font-weight: 500; font-size: 56px; color: var(--ink); }

  .partners__caption { position: absolute; left: 59px; top: 204px; font-size: 15px; letter-spacing: 6px; color: var(--white); }
  .partners__name { position: absolute; left: 59px; top: 226px; font-size: 21px; color: var(--white); }
  .partners__price { position: absolute; right: 50px; top: 206px; font-weight: 700; font-size: 42px; color: var(--white); }

  .perks__main { top: 274px; font-size: 27px; }
  .perks__sub { top: 308px; font-size: 18px; }
  .perks__pack { top: 335px; font-size: 19px; font-weight: 700; }

  .benefits {
    position: absolute; top: 932px; left: 0; width: 100%; text-align: center;
    color: var(--white); font-weight: 700; font-size: 31px; line-height: 39px;
    text-shadow: 0 1px 3px rgba(0,0,0,0.45);
  }
  .benefits__note { display: block; font-weight: 400; font-size: 22px; line-height: 34px; }
  .contact {
    position: absolute; top: 1076px; left: 0; width: 100%; text-align: center;
    color: var(--white); font-weight: 700; font-size: 25px;
    text-shadow: 0 1px 3px rgba(0,0,0,0.45);
  }
</style>
</head>
<body>
  <main class="flyer">
    <div class="flyer__scene" role="img" aria-label="Golf course photo: blue sky, golf bag, flag and a teed-up golf ball on green grass"></div>

    <p class="brand">TAMBORINE RIDGE COUNTRY CLUB</p>
    <h1 class="title">BUSINESS SPONSORSHIP</h1>
    <p class="subtitle">PACKAGE</p>

    <section class="offer">
      <div class="offer__frame"></div>
      <span class="cost__label">COST</span>
      <span class="cost__amount">4500</span>
      <span class="cost__term">+ GST12 MONTHS</span>
      <div class="offer__rule" style="top:100px"></div>

      <p class="promo__line promo__lead">SPONSORSHIP AND PROMOTION</p>
      <p class="promo__line promo__via">VIA <strong>TRCC</strong></p>
      <div class="offer__rule" style="top:194px"></div>

      <span class="partners__caption">CORPORATE</span>
      <span class="partners__name">PARTNERS LISTING</span>
      <span class="partners__price">$1000</span>
      <div class="offer__rule" style="top:264px"></div>

      <p class="promo__line perks__main">FOOD &amp; BEVERAGE</p>
      <p class="promo__line perks__sub">HOUSE ACCOUNT</p>
      <p class="promo__line perks__pack">MEMBERS WELCOME PACK</p>
    </section>

    <p class="benefits">Christmas Party Invite7 Day with<br>Cart Golf Membership10% discount on events and shows
      <span class="benefits__note">Payable over 4 installments</span></p>
    <p class="contact">For more info Call Us Now 555 0192 407&nbsp; or View Our Site www.TRCC.com</p>
  </main>
</body>
</html>
```